SOLVEN TRIDE PORTAL

I'D LIKE TO REDESIGN MY WEBSITE TO MATCH WITH THE NEW BROCHURE WHICH IS ATTACHED. CONTENT AND LOGOS ARE ATTACHED. PLEASE USE WATCH BRAND LOGOS FROM THE BROCHURE
Coded - Design and coding required
1 page

```html
<!DOCTYPE html>
<html lang="en">
<head>
<meta charset="utf-8">
<title>Solven Tride Portal</title>
<link href="https://fonts.googleapis.com/css2?family=Marcellus&family=Poppins:wght@300;400;500;600;700&display=swap" rel="stylesheet">
<style>
:root{
  --ink:#0a0a0a;
  --footer:#151515;
  --gold:#c9a94a;
  --gold-light:#e4d36c;
  --text:#2a2a2a;
  --muted:#6a6a6a;
  --field:#f1f1f2;
  --field-dark:#262626;
  --white:#ffffff;
}
*{box-sizing:border-box;margin:0;padding:0}
html,body{width:1200px;height:3339px;overflow:hidden;background:var(--white)}
body{font-family:"Poppins",sans-serif;color:var(--text)}
.page{position:relative;width:1200px;height:3339px;overflow:hidden}
.abs{position:absolute}
.display{font-family:"Marcellus",serif;font-weight:400;color:var(--ink);text-transform:uppercase}

/* hero */
.hero{left:0;top:0;width:1200px;height:726px;background:radial-gradient(ellipse at 20% 70%,#1c1c1c 0%,#050505 60%),var(--ink)}
.hero-photo{left:570px;top:168px;width:630px;height:467px;background:radial-gradient(ellipse at 55% 50%,#d8cfae 0%,#8d7a45 38%,#2e2812 70%,rgba(0,0,0,0) 85%)}
.brand{left:88px;top:23px;display:flex;align-items:center;gap:16px}
.brand-mark{width:26px;height:26px;background:var(--gold)}
.brand-name{font-family:"Marcellus",serif;font-size:24px;letter-spacing:2px;color:var(--white)}
.nav{left:610px;top:50px;display:flex;gap:30px;font-size:14px;font-weight:500;color:var(--white)}
.nav a{color:inherit;text-decoration:none}
.nav .active{color:var(--gold);position:relative}
.nav .active::before{content:"";position:absolute;left:0;right:0;top:-50px;height:3px;background:var(--gold)}
.hero-kicker{left:90px;top:264px;font-size:20px;color:#d9d9d9}
.hero-title{left:88px;top:294px;font-size:74px;line-height:70px;color:var(--white)}
.hero-rule{left:90px;top:453px;width:428px;height:1px;background:var(--gold)}
.hero-sub{left:88px;top:474px;font-size:18px;font-weight:300;color:#e6e6e6}

/* intro */
.watch-one{left:143px;top:655px;width:304px;height:498px;background:radial-gradient(ellipse at 50% 45%,#1c1c1c 0%,#2d2d2d 32%,#bdbdbd 46%,#e9e9e9 62%,rgba(255,255,255,0) 75%)}
.intro{left:503px;top:842px;width:550px;font-size:15.5px;line-height:26.5px;color:#333}
.intro p+p{margin-top:15px}

/* about */
.dots-area{left:632px;top:1095px;width:122px;height:123px;background:rgba(201,169,74,.25)}
.watch-two{left:690px;top:1146px;width:510px;height:531px;background:linear-gradient(135deg,#1d3a55 0%,#8fb0c8 40%,#2f6b3a 55%,#0c1a2a 100%);box-shadow:0 40px 60px rgba(0,0,0,.28)}
.section-title{font-size:50px;line-height:1}
.about-title{left:88px;top:1248px}
.about-copy{left:88px;top:1305px;width:504px;font-size:12.6px;line-height:20.6px;text-align:justify;color:#333}
.about-copy p+p{margin-top:19px}

/* investments */
.watch-three{left:143px;top:1685px;width:408px;height:431px;background:radial-gradient(ellipse at 50% 40%,#1a2340 0%,#3d3e66 30%,#c98a62 50%,#f0e2d6 62%,rgba(255,255,255,0) 72%)}
.invest-title{left:626px;top:1862px}
.invest-copy{left:626px;top:1917px;width:440px;font-size:12.6px;line-height:20.6px;color:#333}
.invest-copy p+p{margin-top:12px}
.divider{left:88px;top:2116px;width:1023px;height:1px;background:#d9d9d9}

/* sourcing */
.source-title{left:132px;top:2208px;font-size:48px}
.map-photo{left:650px;top:2300px;width:550px;height:350px;background:radial-gradient(ellipse at 50% 50%,#eeeeee 0%,rgba(255,255,255,0) 70%)}
.watch-four{left:700px;top:2255px;width:337px;height:447px;background:radial-gradient(ellipse at 50% 50%,#9fd0da 0%,#8bbfca 28%,#5b3a2c 36%,#d8d8d8 48%,#f3f3f3 62%,rgba(255,255,255,0) 72%)}
.form{left:132px;top:2284px;width:456px}
.label{display:block;font-size:11px;font-weight:600;letter-spacing:.3px;color:#111;text-transform:uppercase;margin-bottom:7px}
.label span{color:var(--gold)}
.row{display:flex;gap:23px;margin-bottom:22px}
.field{flex:1}
.control{height:40px;background:var(--field);display:flex;align-items:center;justify-content:space-between;padding:0 16px;font-size:12.5px;color:#777}
.control svg{width:10px;height:6px}
.textarea{height:117px;align-items:flex-start;padding-top:16px}
.submit{margin-top:37px;height:51px;background:linear-gradient(90deg,#c0a04a 0%,#e3d371 100%);display:flex;align-items:center;justify-content:center;position:relative;color:var(--white);font-weight:700;font-size:18px}
.submit svg{position:absolute;right:20px;top:16px}

/* footer */
.footer{left:0;top:2829px;width:1200px;height:510px;background:var(--footer);color:#cfcfcf}
.f-mark{left:223px;top:2935px;width:34px;height:34px;background:var(--gold)}
.f-name{left:88px;top:3030px;width:306px;text-align:center;font-family:"Marcellus",serif;font-size:25px;letter-spacing:2px;color:var(--white)}
.f-about{left:88px;top:3100px;width:300px;font-size:12.6px;line-height:22px;color:#cfcfcf}
.f-heading{font-family:"Marcellus",serif;font-size:20px;color:var(--white);text-transform:uppercase}
.info-title{left:456px;top:2918px}
.info{left:456px;top:2975px;width:260px}
.info-item{display:flex;gap:10px;margin-bottom:20px;font-size:12.5px;line-height:19px}
.info-item svg{flex:none;margin-top:3px}
.info-item b{display:block;font-weight:600;color:#e6e6e6}
.cform-title{left:744px;top:2918px}
.cform{left:741px;top:2962px;width:371px}
.cform .pair{display:flex;gap:9px;margin-bottom:10px}
.cform .in{flex:1;height:40px;background:var(--field-dark);font-size:12.5px;color:#bdbdbd;padding:13px 14px}
.cform .msg{height:87px}
.send{margin-top:17px;width:113px;height:40px;background:linear-gradient(90deg,#c0a04a,#e3d371);color:var(--white);font-weight:700;font-size:17px;display:flex;align-items:center;justify-content:center}
.f-rule{left:88px;top:3279px;width:1023px;height:1px;background:#333}
.copyright{left:0;top:3298px;width:1200px;text-align:center;font-size:12.5px;color:#e6e6e6}
.to-top{left:1140px;top:3259px;width:40px;height:40px;border-radius:50%;background:#2a2a2a;display:flex;align-items:center;justify-content:center}
</style>
</head>
<body>
<div class="page">

  <header class="abs hero"></header>
  <div class="abs hero-photo" role="img" aria-label="Close-up of a gold chronograph wristwatch with a cream dial"></div>
  <div class="abs brand"><span class="brand-mark"></span><span class="brand-name">SOLVEN TRIDE PORTAL</span></div>
  <nav class="abs nav">
    <a class="active" href="#">HOME</a><a href="#">ABOUT</a><a href="#">INVESTMENTS</a><a href="#">SEARCH WATCHES</a><a href="#">CONTACT</a>
  </nav>
  <div class="abs hero-kicker display" style="color:#d9d9d9">Welcome to</div>
  <h1 class="abs hero-title display" style="color:var(--white)">Solven Tride<br>Portal</h1>
  <div class="abs hero-rule"></div>
  <p class="abs hero-sub">International luxury timepiece supplier</p>

  <div class="abs watch-one" role="img" aria-label="Steel diver's watch with black dial and black bezel"></div>
  <div class="abs intro">
    <p>Simply choose a desired product and allow us to source it for you at the best price and with suitable delivery terms. You will have an option to either collect your purchase from our Cheshire based boutique store, collection points are also in New York City or Dubai or get it delivered to your door via one of our fully insured couriers.</p>
    <p>Making your luxury shopping experience as simple as it can be.</p>
  </div>

  <div class="abs dots-area" role="img" aria-label="Gold dot pattern decoration"></div>
  <div class="abs watch-two" role="img" aria-label="Steel diver's watch with green dial and green bezel on a dark blue background"></div>
  <h2 class="abs section-title display about-title">About us</h2>
  <div class="abs about-copy">
    <p>Solven Tride Portal was first founded in 2018, it has been established as the premier resource to buy and sell premium pre-owned watches. With thousands of watches available from brands including Corvane, Belmont Arche, Halvard Stroem, Dorian Lacaze, Veltris, Maison Orlec and more, plus international locations and clients there's no better place to find a luxury timepiece.</p>
    <p>Outstanding customer service is a mainstay of the Solven Tride ethos. Watch collectors are discerning shoppers, &amp; will accept nothing but the best, which is why customer service has always will be such an important part of the business.</p>
    <p>Our dedicated team of swiss watch experts are perfectly placed to adapt to the ever changing market conditions, giving our investors an 'out of the box' solution. Longevity is as much a focus as immediate success, ensuring you have the best options we can provide tomorrow as well as</p>
  </div>

  <div class="abs watch-three" role="img" aria-label="Rose gold skeleton watch with open movement and blue strap"></div>
  <h2 class="abs section-title display invest-title">Investments</h2>
  <div class="abs invest-copy">
    <p>Interested in becoming part of the ever growing Solven Tride Portal?</p>
    <p>Please leave your details contact form below and one of the team will be in touch to discuss potential options.</p>
  </div>
  <div class="abs divider"></div>

  <h2 class="abs display source-title">Sourcing your watch</h2>
  <div class="abs map-photo" role="img" aria-label="Faint world map background"></div>
  <div class="abs watch-four" role="img" aria-label="Steel chronograph watch with ice blue dial and brown bezel"></div>
  <form class="abs form">
    <div class="row">
      <div class="field"><span class="label">Watch brand<span>*</span></span><div class="control">Select brand<svg viewBox="0 0 10 6"><path d="M1 1l4 4 4-4" fill="none" stroke="#555" stroke-width="1.3"/></svg></div></div>
      <div class="field"><span class="label">Year<span>*</span></span><div class="control">Select year<svg viewBox="0 0 10 6"><path d="M1 1l4 4 4-4" fill="none" stroke="#555" stroke-width="1.3"/></svg></div></div>
    </div>
    <div class="row">
      <div class="field"><span class="label">Material<span>*</span></span><div class="control">Enter material<svg viewBox="0 0 10 6"><path d="M1 1l4 4 4-4" fill="none" stroke="#555" stroke-width="1.3"/></svg></div></div>
      <div class="field"><span class="label">Bezel<span>*</span></span><div class="control">Enter bezel<svg viewBox="0 0 10 6"><path d="M1 1l4 4 4-4" fill="none" stroke="#555" stroke-width="1.3"/></svg></div></div>
    </div>
    <div class="row">
      <div class="field"><span class="label">Strap<span>*</span></span><div class="control" style="padding-left:24px">Select strap<svg viewBox="0 0 10 6"><path d="M1 1l4 4 4-4" fill="none" stroke="#555" stroke-width="1.3"/></svg></div></div>
    </div>
    <div class="field"><span class="label">Message<span>*</span></span><div class="control textarea" style="padding-left:24px">Type your text...</div></div>
    <div class="submit">SUBMIT NOW<svg width="22" height="20" viewBox="0 0 22 20"><path d="M1 9L21 1l-5 18-6-6-4 5v-7z" fill="none" stroke="#fff" stroke-width="2" stroke-linejoin="round"/></svg></div>
  </form>

  <footer class="abs footer"></footer>
  <div class="abs f-mark"></div>
  <div class="abs f-name">SOLVEN TRIDE PORTAL</div>
  <p class="abs f-about">Alternatively please feel free to contact us on 01615550192 For a more detailed chat with one of our timepiece specialists</p>

  <h3 class="abs f-heading info-title">Contact info</h3>
  <div class="abs info">
    <div class="info-item"><svg width="12" height="12" viewBox="0 0 12 12"><path d="M2.5 1l2 2.5-1 1.2a7 7 0 003.8 3.8l1.2-1 2.5 2-1 1.5C5 11 1 7 1 2z" fill="var(--gold)"/></svg><div><b>PHONE*</b>1615550192</div></div>
    <div class="info-item"><svg width="12" height="10" viewBox="0 0 12 10"><rect x="0.5" y="0.5" width="11" height="9" fill="var(--gold)"/><path d="M1 1l5 4 5-4" fill="none" stroke="#151515"/></svg><div><b>Email</b>sales@solventride-portal.co.uk</div></div>
    <div class="info-item"><svg width="10" height="13" viewBox="0 0 10 13"><path d="M5 0a5 5 0 015 5c0 3-5 8-5 8S0 8 0 5a5 5 0 015-5z" fill="var(--gold)"/><circle cx="5" cy="5" r="1.8" fill="#151515"/></svg><div><b>Address</b>Some address line goes here<br>city name country</div></div>
  </div>

  <h3 class="abs f-heading cform-title">Contact form</h3>
  <div class="abs cform">
    <div class="pair"><div class="in">First Name</div><div class="in">Last Name</div></div>
    <div class="pair"><div class="in">Phone Number</div><div class="in">Email</div></div>
    <div class="in msg">Message</div>
    <div class="send">SEND</div>
  </div>

  <div class="abs f-rule"></div>
  <p class="abs copyright">© Copyright 2022 Solven Tride Portal All Right Reserved</p>
  <div class="abs to-top"><svg width="10" height="6" viewBox="0 0 10 6"><path d="M1 5l4-4 4 4" fill="none" stroke="#ccc" stroke-width="1.3"/></svg></div>

</div>
</body>
</html>
```